Gala Dinner Flyer for State Water Polo Association

We need a promotional flyer for the "2016 Ripple Soirée" - a fundraising gala dinner for Aquaclash Union in Victoria to distribute to our members.

The details for the event are as follows:

Date: Saturday 16th April 2016
Time: 7pm to Midnight
Venue: Lagoon Hall B, Marlow Quay, 47 Tidewell Parade, Sandmere 3012
Cost: $150 per person
Details: Canapés on arrival followed by a three course dinner, with premium beverages throughout the evening.
RSVP: Friday 8th April 2016
Dress Code: Black Tie
For tickets for to www.ticketnook.com.au/tickets/event/ripplesoiree

We also require an event logo with a minimum height of 200px, and event background with a minimum width of 1200px and height of 800px, and flyer image with a minimum width of 620px and height of 874px.

I have attached a number of logos we need incorporated along with last years invitation and a few photos from last years event.

We would like to use designs that use water and the colour blue.

The final design should communicate elegance and high class

Target Market(s)

25-60 year old Men and Women from affluent families

Industry/Entity Type

Promotional

Colors
1861ab
3277b5
85acd3
cedeed
ffffff

Requirements
Must have
• Aquaclash Union Victoria Logo, Victorian Herons Logo, mindharbor Logo & Corvell Holdings Logo

```html
<!DOCTYPE html>
<html lang="en">
<head>
<meta charset="utf-8">
<title>2016 Ripple Soirée – Gala Dinner Flyer</title>
<link rel="stylesheet" href="https://fonts.googleapis.com/css2?family=Great+Vibes&family=Cinzel:wght@600&family=Lato:wght@400;700&display=swap">
<style>
  :root {
    --navy-deep: #050d24;
    --navy: #0b1f4a;
    --royal: #1861ab;
    --mid-blue: #3277b5;
    --sky: #85acd3;
    --ice: #cedeed;
    --white: #ffffff;
    --accent-blue: #6fc3ff;
    --ribbon: #b3172a;
    --ribbon-dark: #7a0d1a;
    --page-bg: #e9edf2;
    --footer-ink: #1d3b73;
  }
  * { box-sizing: border-box; margin: 0; padding: 0; }
  html, body { width: 1200px; height: 800px; overflow: hidden; }
  body { background: var(--page-bg); font-family: "Lato", sans-serif; position: relative; }

  .flyer {
    position: absolute; left: 334px; top: 20px;
    width: 532px; height: 760px; overflow: hidden;
    background: var(--navy-deep);
    box-shadow: 0 6px 24px rgba(0,0,0,.25);
  }
  .flyer-backdrop {
    position: absolute; inset: 0 0 72px 0;
    background:
      radial-gradient(ellipse 60% 18% at 30% 2%, rgba(255,255,255,.85), transparent 70%),
      radial-gradient(ellipse 40% 14% at 85% 3%, rgba(220,240,255,.8), transparent 70%),
      linear-gradient(180deg, #3d8fd8 0%, var(--royal) 14%, var(--navy) 34%, #0a1a3c 48%, #060f26 62%, var(--navy-deep) 100%);
  }
  .photo { position: absolute; }
  .photo-band {
    left: 0; top: 491px; width: 207px; height: 197px;
    background: linear-gradient(160deg, #1c2a44 0%, #0c1529 60%, #050a18 100%);
  }
  .photo-singer {
    right: 0; top: 485px; width: 138px; height: 203px;
    background: radial-gradient(ellipse 70% 60% at 70% 50%, #3c4f55 0%, #1b2a3a 55%, transparent 100%);
  }

  .invite-band {
    position: absolute; left: 0; top: 81px; width: 262px; height: 36px;
    background: linear-gradient(90deg, rgba(8,22,52,.85), rgba(8,22,52,.6));
    color: var(--white); font-size: 19px; letter-spacing: .2px;
    display: flex; align-items: center; padding-left: 34px;
  }
  .event-year {
    position: absolute; left: 268px; top: 40px;
    font-family: "Great Vibes", cursive; font-size: 88px; color: var(--white);
    text-shadow: 0 2px 6px rgba(0,0,0,.35);
  }
  .event-name {
    position: absolute; left: 0; right: 0; top: 130px; text-align: center;
    font-family: "Great Vibes", cursive; font-size: 92px; line-height: 1.2; color: var(--white);
    text-shadow: 0 3px 8px rgba(0,0,0,.4);
  }

  .date-ribbon { position: absolute; left: 78px; top: 252px; width: 382px; height: 80px; }
  .date-ribbon svg { position: absolute; inset: 0; }
  .date-ribbon-text {
    position: absolute; left: 22px; top: 22px; width: 340px; text-align: center;
    font-family: "Cinzel", serif; font-weight: 600; font-size: 13.5px; color: var(--white);
    transform: rotate(4deg); white-space: nowrap;
  }

  .info-block {
    position: absolute; left: 72px; width: 388px; text-align: center;
    background: rgba(5,12,32,.55); color: var(--white);
    font-size: 14.5px; line-height: 18.5px; padding: 2px 8px 3px;
  }
  .info-label { color: var(--accent-blue); font-weight: 700; font-size: 15px; }
  .info-venue { top: 330px; }
  .info-details { top: 404px; }
  .info-cost { top: 496px; }
  .info-rsvp { top: 550px; }
  .ticket-link {
    position: absolute; left: 0; right: 0; top: 623px; text-align: center;
    color: var(--accent-blue); font-weight: 700; font-size: 13.5px;
  }

  .partner-strip {
    position: absolute; left: 0; bottom: 0; width: 100%; height: 72px;
    background: var(--white);
    display: flex; align-items: center; justify-content: space-around; padding: 0 36px;
  }
  .partner { display: flex; align-items: center; gap: 6px; color: var(--footer-ink); font-size: 12px; font-weight: 700; }
  .partner-dot { width: 14px; height: 14px; border-radius: 50%; background: var(--royal); }
  .partner-corporate { font-weight: 400; font-size: 15px; letter-spacing: 2.5px; text-transform: uppercase; }
</style>
</head>
<body>
  <main class="flyer">
    <div class="flyer-backdrop" role="img" aria-label="Gala ballroom under blue stage lights with guests at dinner tables"></div>
    <div class="photo photo-band" role="img" aria-label="Live band performing on stage"></div>
    <div class="photo photo-singer" role="img" aria-label="Singer with microphone in a sequinned dress"></div>

    <div class="invite-band">YOU’RE INVITED TO THE</div>
    <div class="event-year">2016</div>
    <h1 class="event-name">Ripple Soirée</h1>

    <div class="date-ribbon">
      <svg viewBox="0 0 382 80" aria-hidden="true">
        <path d="M8 18 L20 30 L8 46 L40 48 L40 22 Z" fill="var(--ribbon-dark)"/>
        <path d="M330 50 L372 58 L360 70 L376 80 L340 78 Z" fill="var(--ribbon-dark)"/>
        <path d="M22 14 Q190 10 368 44 L362 72 Q190 40 24 46 Z" fill="var(--ribbon)"/>
      </svg>
      <div class="date-ribbon-text">Saturday 16th April 2016 | 7pm to Midnight</div>
    </div>

    <section class="info-block info-venue">
      <div class="info-label">Venue:</div>
      <div>Lagoon Hall B, Marlow Quay 47 Tidewell Parade,<br>Sandmere VIC 3012</div>
    </section>
    <section class="info-block info-details">
      <div class="info-label">Details:</div>
      <div>Canapés on arrival followed by a three course<br>dinner, with premium beverages throughout the<br>evening</div>
    </section>
    <section class="info-block info-cost">
      <div class="info-label">Cost:</div>
      <div>$150 per person</div>
    </section>
    <section class="info-block info-rsvp">
      <div class="info-label">RSVP:</div>
      <div>Friday 8th April 2016<br>Dress: Black Tie</div>
    </section>
    <p class="ticket-link">For tickets go to www.ticketnook.com.au/tickets/event/ripplesoiree</p>

    <footer class="partner-strip">
      <div class="partner"><span class="partner-dot"></span>Victorian Herons</div>
      <div class="partner">Aquaclash Union Victoria</div>
      <div class="partner partner-corporate">Corvell Holdings</div>
    </footer>
  </main>
</body>
</html>
```